Bref créative
Business card and stationary for Maplecrest Vision Studio Eye Clinic
Maplecrest Vision Studio / (Clear Sight Daily)
Professional
Dr. Marcus Pell, O.D.
Optometric Physician
Bayline Office
2864 Larkwood Ave
Harborview, FL. 34901
Emergency:813-555-0487
maplecrestvisionstudiohub@mailbox-demo.net
www.maplecrestvisionstudio-demo.com
Appointment
Date:_______ @ ______ AM / PM
WWW.MAPLECRESTVISIONSTUDIO-DEMO.COM
if unable to keep appointment kindly give 24 hours notice.
I need a business card and brochure made for my office with the new logo.

```html
<!DOCTYPE html>
<html lang="en">
<head>
<meta charset="utf-8">
<title>Maplecrest Vision Studio – Business Card</title>
<link href="https://fonts.googleapis.com/css2?family=Lato:ital,wght@0,300;0,400;0,700;1,400&display=swap" rel="stylesheet">
<style>
  :root {
    --bg: #e4e5e7;
    --paper: #ffffff;
    --brand-blue: #2b93c6;
    --ink: #2a2f36;
    --muted: #6d747c;
    --rule: #d5d8dc;
    --frame-dark: #34373b;
  }
  * { box-sizing: border-box; margin: 0; padding: 0; }
  html, body { width: 1200px; height: 895px; overflow: hidden; }
  body {
    background: var(--bg);
    font-family: "Lato", sans-serif;
    color: var(--ink);
    display: flex;
    align-items: center;
    justify-content: center;
    gap: 50px;
  }
  .card {
    width: 540px;
    height: 310px;
    padding: 14px;
    box-shadow: 0 6px 18px rgba(0,0,0,0.12);
  }
  .card--front { background: var(--brand-blue); }
  .card--back { background: var(--frame-dark); }
  .card__face {
    width: 100%;
    height: 100%;
    background: var(--paper);
    display: flex;
  }
  /* front */
  .brand-block {
    width: 52%;
    display: flex;
    flex-direction: column;
    justify-content: center;
    padding-left: 34px;
  }
  .wordmark {
    display: flex;
    align-items: center;
    gap: 10px;
  }
  .wordmark__dot {
    width: 16px; height: 16px;
    border-radius: 50%;
    background: var(--brand-blue);
    flex: none;
  }
  .wordmark__name {
    font-weight: 700;
    font-size: 22px;
    letter-spacing: 1.5px;
    line-height: 1.15;
    color: var(--ink);
    text-transform: uppercase;
  }
  .tagline {
    margin-top: 10px;
    padding-left: 26px;
    font-style: italic;
    font-size: 14px;
    color: var(--muted);
  }
  .contact-block {
    width: 48%;
    border-left: 1px solid var(--rule);
    margin: 40px 0;
    padding-left: 22px;
    padding-right: 8px;
    display: flex;
    flex-direction: column;
    justify-content: center;
  }
  .person__name { font-weight: 700; font-size: 14px; color: var(--brand-blue); }
  .person__title { font-size: 11px; color: var(--muted); margin-bottom: 12px; }
  .contact-list { list-style: none; }
  .contact-list li {
    display: flex;
    align-items: flex-start;
    gap: 7px;
    font-size: 9.5px;
    line-height: 1.35;
    margin-bottom: 5px;
    color: var(--ink);
    overflow-wrap: anywhere;
  }
  .contact-list svg { flex: none; margin-top: 1px; }
  /* back */
  .card--back .card__face {
    flex-direction: column;
    align-items: center;
    justify-content: center;
  }
  .card--back .wordmark__name { font-size: 26px; }
  .site-url {
    margin-top: 34px;
    font-size: 10px;
    letter-spacing: 2.5px;
    color: var(--brand-blue);
  }
</style>
</head>
<body>
  <section class="card card--front">
    <div class="card__face">
      <div class="brand-block">
        <div class="wordmark">
          <span class="wordmark__dot"></span>
          <span class="wordmark__name">Maplecrest<br>Vision Studio</span>
        </div>
        <p class="tagline">Clear Sight Daily</p>
      </div>
      <div class="contact-block">
        <p class="person__name">Dr. Marcus Pell, O.D.</p>
        <p class="person__title">Optometric Physician</p>
        <ul class="contact-list">
          <li>
            <svg width="12" height="12" viewBox="0 0 12 12"><circle cx="6" cy="6" r="6" fill="var(--brand-blue)"/><path d="M6 2.6a2.2 2.2 0 0 0-2.2 2.2C3.8 6.5 6 9.4 6 9.4s2.2-2.9 2.2-4.6A2.2 2.2 0 0 0 6 2.6z" fill="#fff"/></svg>
            <span>Bayline Office 2864 Larkwood Ave<br>Harborview, FL. 34901</span>
          </li>
          <li>
            <svg width="12" height="12" viewBox="0 0 12 12"><circle cx="6" cy="6" r="6" fill="var(--brand-blue)"/><path d="M4 3l1.2 1.5-.6.8a4 4 0 0 0 2.1 2.1l.8-.6L9 8l-.8.9C6 8.7 3.3 6 3.1 3.8z" fill="#fff"/></svg>
            <span>813-555-0487</span>
          </li>
          <li>
            <svg width="12" height="12" viewBox="0 0 12 12"><circle cx="6" cy="6" r="6" fill="var(--brand-blue)"/><path d="M4 3l1.2 1.5-.6.8a4 4 0 0 0 2.1 2.1l.8-.6L9 8l-.8.9C6 8.7 3.3 6 3.1 3.8z" fill="#fff"/></svg>
            <span>813-555-0192</span>
          </li>
          <li>
            <svg width="12" height="12" viewBox="0 0 12 12"><circle cx="6" cy="6" r="6" fill="var(--brand-blue)"/><rect x="3" y="4" width="6" height="4.2" fill="#fff"/><path d="M3 4l3 2.3L9 4" stroke="var(--brand-blue)" stroke-width=".7" fill="none"/></svg>
            <span>maplecrestvisionstudiohub@mailbox-demo.net</span>
          </li>
          <li>
            <svg width="12" height="12" viewBox="0 0 12 12"><circle cx="6" cy="6" r="6" fill="var(--brand-blue)"/><circle cx="6" cy="6" r="3" fill="none" stroke="#fff" stroke-width=".8"/><path d="M3 6h6M6 3v6" stroke="#fff" stroke-width=".6"/></svg>
            <span>www.maplecrestvisionstudio-demo.com</span>
          </li>
        </ul>
      </div>
    </div>
  </section>

  <section class="card card--back">
    <div class="card__face">
      <div class="wordmark">
        <span class="wordmark__dot"></span>
        <span class="wordmark__name">Maplecrest<br>Vision Studio</span>
      </div>
      <p class="site-url">WWW.MAPLECRESTVISIONSTUDIO-DEMO.COM</p>
    </div>
  </section>
</body>
</html>
```